Please make an eye catching and elegant flyer. Here is the content
Delphine's 70th Birthday Bash
Friday September 13th, 2024
8pm - 12midnight
Location:
Corvel's Oakland
47 Linden Ave, Oakland, CA 94612
For more information and to RSVP contact 916-482-3107 or 510-617-2043

Colors
FFF300
FFF600
FEFA6F
FFFEC7
FFFEE8
EB3D1F
EC4F4E
F09395
F8D3D4
FCEDEE
A7469A
B969AE
D3A5CF
EDDBEB
F8F0F9

Requirements
Nice to have
• Her favorite colors are royal purple, white, red. and gold. You don't have to use all of these colors yet at least a couple would be nice.

```html
<!DOCTYPE html>
<html lang="en">
<head>
<meta charset="utf-8">
<title>Delphine's 70th Birthday Celebration</title>
<link href="https://fonts.googleapis.com/css2?family=Cinzel:wght@600;700;800;900&family=Montserrat:wght@500;600&display=swap" rel="stylesheet">
<style>
  :root {
    --plum-deep: #2a0412;
    --plum: #5a0b3a;
    --royal-purple: #7a1f78;
    --magenta: #c0206a;
    --crimson: #b3122a;
    --flame: #eb3d1f;
    --orange: #f0641e;
    --gold-light: #fff3a8;
    --gold: #f0c24a;
    --gold-deep: #c98a1c;
    --white: #ffffff;
    --blush: #fcedee;
  }
  * { margin: 0; padding: 0; box-sizing: border-box; }
  html, body { width: 923px; height: 1200px; overflow: hidden; background: var(--plum-deep); }
  .flyer {
    position: relative;
    width: 923px; height: 1200px; overflow: hidden;
    background:
      radial-gradient(ellipse 320px 420px at 800px 820px, rgba(240,100,30,.85), transparent 70%),
      radial-gradient(ellipse 380px 380px at 80px 760px, rgba(122,31,120,.8), transparent 70%),
      linear-gradient(180deg, var(--plum) 0%, #6a0d36 50%, #3a0618 80%, var(--plum-deep) 100%);
    font-family: 'Cinzel', serif;
  }
  .backdrop { position: absolute; top: 0; left: 0; width: 923px; height: 660px; }
  .backdrop__panel { position: absolute; top: 0; height: 100%; }
  .backdrop__panel--1 { left: 0; width: 216px; background: linear-gradient(180deg, #4a1658, #8b1f72 55%, rgba(122,31,120,0)); }
  .backdrop__panel--2 { left: 216px; width: 235px; background: linear-gradient(180deg, #6a0f3a, #c3225f 50%, rgba(192,32,106,0)); }
  .backdrop__panel--3 { left: 451px; width: 256px; background: linear-gradient(180deg, #7a1a3a, #b8306a 55%, rgba(180,40,90,0)); }
  .backdrop__panel--4 { left: 707px; width: 216px; background: linear-gradient(180deg, #6a1838, #c43a6a 45%, rgba(235,80,40,.6)); }
  .portrait { position: absolute; }
  .portrait--red {
    left: 150px; top: 205px; width: 350px; height: 445px;
    border-radius: 140px 140px 20px 20px;
    background: linear-gradient(180deg, #6a2418 0%, #b3122a 35%, #8c0c1c 80%, rgba(140,12,28,0) 100%);
  }
  .portrait--green {
    left: 470px; top: 210px; width: 275px; height: 530px;
    border-radius: 120px 120px 30px 30px;
    background: linear-gradient(180deg, #7a3a24 0%, #2f9a62 30%, #e8a020 60%, #2f9a62 85%, rgba(47,154,98,0) 100%);
    opacity: .9;
  }
  .title-name {
    position: absolute; left: 216px; width: 300px; top: 616px; text-align: center; z-index: 3;
    font-weight: 800; font-size: 36px; line-height: 40px; letter-spacing: 0;
    color: var(--gold);
  }
  .flare {
    position: absolute; left: 330px; top: 668px; width: 200px; height: 3px; z-index: 3;
    background: linear-gradient(90deg, transparent, #ffd27a 50%, transparent);
    box-shadow: 0 0 12px #ffb040;
  }
  .age {
    position: absolute; left: 232px; top: 626px; z-index: 2;
    font-weight: 700; font-size: 390px; line-height: 1; letter-spacing: 0;
    background: linear-gradient(160deg, var(--gold-light) 0%, var(--gold) 35%, var(--gold-deep) 65%, #f5d36a 100%);
    -webkit-background-clip: text; background-clip: text; color: transparent;
  }
  .age-suffix {
    position: absolute; left: 672px; top: 908px;
    font-weight: 800; font-size: 22px; line-height: 24px; color: var(--gold);
  }
  .occasion {
    position: absolute; left: 177px; top: 875px; width: 357px; height: 85px;
    border: 2px solid var(--gold); border-radius: 24px;
    padding: 13px 0 0 19px; z-index: 3;
  }
  .occasion__line1 { font-weight: 900; font-size: 29px; color: var(--gold); line-height: 1; letter-spacing: 1.5px; }
  .occasion__line2 { font-weight: 900; font-size: 20px; color: var(--gold); line-height: 1; margin-top: 7px; letter-spacing: 1px; }
  .details { position: absolute; top: 977px; text-align: center; color: var(--white); }
  .details--date { left: 193px; width: 310px; }
  .details--time { left: 488px; width: 270px; }
  .details__label {
    display: inline-block; background: var(--gold); color: var(--crimson);
    font-weight: 800; font-size: 19px; line-height: 22px; padding: 0 4px; border-radius: 3px;
  }
  .details__value { font-weight: 700; font-size: 22px; line-height: 22px; margin-top: 1px; letter-spacing: .8px; }
  .venue {
    position: absolute; left: 213px; top: 1051px; width: 497px; height: 50px;
    background: linear-gradient(90deg, rgba(140,10,30,.7), var(--crimson) 60%, var(--flame));
    text-align: center; color: var(--gold); font-weight: 800; font-size: 19px; line-height: 20px;
    padding-top: 5px; letter-spacing: 1px;
  }
  .divider { position: absolute; left: 186px; top: 1113px; width: 551px; height: 1px; background: rgba(255,255,255,.85); }
  .rsvp {
    position: absolute; left: 0; width: 923px; top: 1124px; text-align: center;
    font-family: 'Montserrat', sans-serif; color: var(--blush); font-weight: 600;
  }
  .rsvp__text { font-size: 14.5px; line-height: 18px; letter-spacing: .2px; }
  .rsvp__phones { font-size: 14px; line-height: 18px; letter-spacing: 6.5px; margin-top: 2px; }
</style>
</head>
<body>
<main class="flyer">
  <div class="backdrop" role="img" aria-label="Collage of dance performance photos in purple and pink tones">
    <div class="backdrop__panel backdrop__panel--1"></div>
    <div class="backdrop__panel backdrop__panel--2"></div>
    <div class="backdrop__panel backdrop__panel--3"></div>
    <div class="backdrop__panel backdrop__panel--4"></div>
  </div>
  <div class="portrait portrait--red" role="img" aria-label="Portrait of the guest of honour in a red lace gown and gold head wrap"></div>
  <div class="portrait portrait--green" role="img" aria-label="The guest of honour dancing joyfully in a green and orange print dress"></div>

  <h1 class="title-name">DELPHINE'S</h1>
  <div class="flare"></div>
  <div class="age">70</div>
  <div class="age-suffix">TH</div>
  <div class="occasion">
    <div class="occasion__line1">BIRTHDAY</div>
    <div class="occasion__line2">CELEBRATION</div>
  </div>

  <section class="details details--date">
    <span class="details__label">DATE</span>
    <p class="details__value">FRIDAY SEPTEMBER<br>13TH, 2024</p>
  </section>
  <section class="details details--time">
    <span class="details__label">TIME</span>
    <p class="details__value">8PM TO<br>12MIDNIGHT</p>
  </section>

  <div class="venue">VANUE : CORVEL'S OAKLAND<br>47 LINDEN AVE, OAKLAND, CA 94612</div>
  <div class="divider"></div>
  <div class="rsvp">
    <p class="rsvp__text">FOR MORE INFORMATION AND TO RSVP CONTACT</p>
    <p class="rsvp__phones">916-482-3107 OR 510-617-2043</p>
  </div>
</main>
</body>
</html>
```